Trelvane Summit Flyer to describe services

I provide data abstraction and consulting services to hospitals that are participating in an accreditation program for their bariatric surgery program. I need a flyer that I can hand out to potential clients that describes the services that I offer. I am attaching an info sheet that has the information on the services I offer. (One exception is that I no longer offer the remote dietitian services listed on the flyer) . I am also including a file with my logo. I would like this flyer to hand out at conferences where I meet people that might not be familiar with my business or who are not knowledgeable of how my services might benefit them. The most important service that I offer is the data abstraction subcontracting. I will provide a PPT that will provide further info on this service.

Target Market(s)

Bariatric program directors and surgeons

Industry/Entity Type

Healthcare

Font styles to use
Serif
Sans Serif

Colors

Designer to choose colors to be used in the design.

Requirements
Must have
• a description of the services I offer
• how subcontracting will benefit them and save them money
• something noting my experience as I am one of the most experienced professionals in this field of bariatric surgery accreditation
Nice to have
• I am not a designer and created the flyer that I have provided. I realize it is not very professional and would like something that looks fresh and professional.
Should not have
• I don't want it to be too wordy and yet it needs to have a description of services offered. I want to include the yellow in my logo, but the flyer sample I have given you has waaaaay too much yellow and want to tone that down!

```html
<!DOCTYPE html>
<html lang="en">
<head>
<meta charset="utf-8">
<title>Trelvane Summit Consulting – Services Flyer</title>
<link rel="stylesheet" href="https://fonts.googleapis.com/css2?family=Montserrat:wght@600;700;800&family=Nunito+Sans:ital,wght@0,400;0,600;0,700;1,400;1,700&display=swap">
<style>
:root{
  --yellow:#f9d400;
  --ink:#1d1d1f;
  --muted:#3a3a3a;
  --page:#ffffff;
  --stage:#ffffff;
  --rule:#e2e2e2;
}
*{box-sizing:border-box;margin:0;padding:0}
html,body{width:1200px;height:1000px;overflow:hidden;background:var(--stage)}
body{font-family:"Nunito Sans",Arial,sans-serif;color:var(--ink);position:relative}
.flyer{position:absolute;left:212px;top:5px;width:763px;height:985px;background:var(--page);box-shadow:0 2px 8px rgba(0,0,0,.35);overflow:hidden}
.flyer *{position:absolute}
.hero{left:0;top:0;width:763px;height:290px;background:linear-gradient(180deg,#fff 0%,#f0f0f0 100%)}
.portrait{left:455px;top:35px;width:308px;height:255px;background:radial-gradient(ellipse at 55% 38%,#e8d3c0 0%,#d9b98e 26%,#2f56b0 60%,#1e3f94 100%)}
.brand{left:33px;top:50px;display:flex;align-items:center;gap:8px;font-family:"Montserrat",sans-serif;font-weight:800;font-size:22px;letter-spacing:-.3px;color:var(--ink);white-space:nowrap}
.brand .mark{position:static;width:13px;height:13px;background:var(--yellow)}
.brand span{position:static}
.headline{left:33px;top:138px;font-size:40px;font-weight:400;color:var(--ink);white-space:nowrap;letter-spacing:-.3px}
.program{left:33px;top:190px;font-family:"Montserrat",sans-serif;font-weight:800;font-size:50px;color:var(--yellow);line-height:1}
.hero-rule{left:33px;top:244px;width:85px;height:3px;background:var(--ink)}
.website{left:33px;top:256px;font-size:17px;color:var(--ink)}
.experience{left:0;top:290px;width:763px;height:102px;background:var(--yellow)}
.experience p{position:static;margin:24px auto 0;width:620px;text-align:center;font-style:italic;font-size:15px;line-height:17px;text-transform:uppercase;color:var(--ink)}
.experience .rule{left:338px;top:84px;width:86px;height:3px;background:var(--ink)}
.section-title{left:0;top:410px;width:763px;text-align:center;font-family:"Montserrat",sans-serif;font-weight:800;font-size:30px;color:var(--yellow)}
.divider{left:383px;top:460px;width:1px;height:440px;background:var(--rule)}
.service-icon{width:58px;height:58px}
.service-name{font-family:"Montserrat",sans-serif;font-weight:700;font-size:18px;text-align:center;color:var(--ink);white-space:nowrap}
.service-text{font-size:11.4px;line-height:14.2px;text-transform:uppercase;text-align:justify;text-align-last:center;color:var(--muted)}
.sub-title{font-style:italic;font-weight:700;font-size:12.5px;text-align:center;color:var(--ink)}
.checks{list-style:none;font-size:11.3px;line-height:13.4px;color:var(--muted)}
.checks li{position:relative;padding-left:14px;margin-bottom:4px}
.checks.loose li{margin-bottom:0;line-height:17px}
.checks li::before{content:"";position:absolute;left:1px;top:2px;width:5px;height:9px;border:solid var(--ink);border-width:0 2px 2px 0;transform:rotate(40deg)}
.contact-bar{left:0;top:910px;width:763px;height:75px;background:var(--yellow)}
.contact-person{left:36px;top:24px;display:flex;gap:12px;align-items:flex-start}
.contact-person svg,.contact-person div{position:static}
.contact-person .name{font-weight:700;font-size:13px;line-height:14px}
.contact-person .role{font-size:13px;line-height:14px}
.contact-phone{left:258px;top:24px;display:flex;gap:10px;align-items:center;font-family:"Montserrat",sans-serif;font-weight:700;font-size:22px}
.contact-email{left:470px;top:30px;display:flex;gap:8px;align-items:center;font-weight:700;font-size:13px}
.contact-phone *,.contact-email *{position:static}
</style>
</head>
<body>
<main class="flyer">
  <section class="hero"></section>
  <div class="portrait" role="img" aria-label="Portrait photo of the consultant in a blue top and pearl necklace"></div>
  <div class="brand"><span class="mark"></span><span>TRELVANE SUMMIT CONSULTING</span></div>
  <h1 class="headline">Helping you navigate</h1>
  <div class="program">BSQAP</div>
  <div class="hero-rule"></div>
  <div class="website">trelvanesummitconsulting.com</div>

  <section class="experience">
    <p>18 years of metabolic &amp; bariatric surgery experience, developing quality improvement processes that will track performance improvement, safety, and patient outcomes.</p>
    <div class="rule"></div>
  </section>

  <h2 class="section-title">SERVICES</h2>
  <div class="divider"></div>

  <svg class="service-icon" style="left:167px;top:448px" viewBox="0 0 58 58"><circle cx="29" cy="29" r="27" fill="none" stroke="var(--yellow)" stroke-width="2.5"/><g fill="var(--yellow)"><circle cx="23" cy="20" r="4"/><circle cx="35" cy="20" r="4"/><rect x="17" y="25" width="24" height="6" rx="2"/><rect x="15" y="31" width="28" height="4"/><rect x="17" y="35" width="3" height="8"/><rect x="38" y="35" width="3" height="8"/></g></svg>
  <h3 class="service-name" style="left:36px;top:506px;width:320px">BSDR STAFFING</h3>
  <p class="service-text" style="left:36px;top:531px;width:324px">Maintain compliance with a certified data abstractor who will be a member of your MBS team, provide consistent leadership, assist in development of QI projects utilizing your program data, perform routine quality audits and remotely attend all MBS committee meetings.</p>
  <p class="sub-title" style="left:36px;top:624px;width:320px">Why Subcontract the BSDR?</p>
  <ul class="checks" style="left:44px;top:643px;width:310px">
    <li>It's Cost Effective - facility pays no employee benefits, freeing up valuable resources for other program needs</li>
    <li>Pricing is based on facility volume</li>
    <li>Experienced and Certified BSDR's provide leadership and ensure consistent high quality data abstraction and compliance with accreditation standards</li>
    <li>Ensures emphasis on QI/PI as a continuous process</li>
  </ul>

  <svg class="service-icon" style="left:161px;top:758px" viewBox="0 0 58 58"><circle cx="29" cy="29" r="27" fill="none" stroke="var(--yellow)" stroke-width="2.5"/><g fill="var(--yellow)"><circle cx="22" cy="19" r="5"/><path d="M13 42v-10a6 6 0 0 1 6-6h6a6 6 0 0 1 6 6v10z"/><rect x="31" y="25" width="13" height="16" rx="1"/></g><path d="M34 33l3 3 5-6" stroke="#fff" stroke-width="2" fill="none"/></svg>
  <h3 class="service-name" style="left:36px;top:816px;width:330px">MOCK SITE INSPECTIONS</h3>
  <p class="service-text" style="left:32px;top:842px;width:328px">A one-day rigorous evaluation that mirrors the BSQAP site survey process and evaluates accreditation readiness by providing a critical assessment of all BSQAP standards.</p>

  <svg class="service-icon" style="left:532px;top:448px" viewBox="0 0 58 58"><circle cx="29" cy="29" r="27" fill="none" stroke="var(--yellow)" stroke-width="2.5"/><g fill="none" stroke="var(--yellow)" stroke-width="2"><rect x="17" y="22" width="24" height="20"/><rect x="23" y="14" width="12" height="8"/><rect x="26" y="34" width="6" height="8"/><path d="M21 27h4M33 27h4M21 31h4M33 31h4M29 16v4M27 18h4"/></g></svg>
  <h3 class="service-name" style="left:400px;top:506px;width:335px">PROGRAM DEVELOPMENT</h3>
  <p class="service-text" style="left:404px;top:530px;width:326px">Assistance developing all aspects of a new or struggling weight loss surgery program that will ensure eventual BSQAP accreditation.</p>
  <ul class="checks" style="left:420px;top:576px;width:320px">
    <li>On-site and/or remote assistance</li>
    <li>Guidance in development of policies and procedures and job descriptions</li>
    <li>Templates for customizing clinical pathways</li>
    <li>Development of staff education modules</li>
    <li>Establish protocols that ensure efficient business practices</li>
  </ul>

  <svg class="service-icon" style="left:530px;top:679px" viewBox="0 0 58 58"><circle cx="29" cy="29" r="27" fill="none" stroke="var(--yellow)" stroke-width="2.5"/><g fill="none" stroke="var(--yellow)" stroke-width="2"><path d="M19 14h15l6 6v24H19z"/><path d="M23 24h8M23 29h8M23 34h6"/><path d="M32 40l9-11 3 3-9 11-4 1z"/></g></svg>
  <h3 class="service-name" style="left:400px;top:738px;width:335px">PROGRAM ASSESMENT</h3>
  <p class="service-text" style="left:400px;top:762px;width:335px;text-align:center">A 2-day on-site assessment of the bariatric program to include:</p>
  <ul class="checks loose" style="left:420px;top:799px;width:320px">
    <li>Compliance with BSQAP Standards and Best Practices</li>
    <li>Business strategies</li>
    <li>Process for collecting and utilizing outcomes data</li>
    <li>Comprehensive post-assessment review will provide guidance, solutions, timelines and suggest opportunities for improvement</li>
  </ul>

  <footer class="contact-bar">
    <div class="contact-person">
      <svg width="12" height="16" viewBox="0 0 12 16"><circle cx="6" cy="4" r="3.5" fill="var(--ink)"/><path d="M0 16v-4a5 5 0 0 1 5-5h2a5 5 0 0 1 5 5v4z" fill="var(--ink)"/></svg>
      <div><div class="name">Marla Dentcourt, RN, CBN</div><div class="role">Bariatric Program Consultant</div></div>
    </div>
    <div class="contact-phone">
      <svg width="16" height="16" viewBox="0 0 24 24"><path fill="var(--ink)" d="M6.6 10.8a15.1 15.1 0 0 0 6.6 6.6l2.2-2.2c.3-.3.7-.4 1-.2 1.1.4 2.3.6 3.6.6.6 0 1 .4 1 1V20c0 .6-.4 1-1 1A17 17 0 0 1 3 4c0-.6.4-1 1-1h3.5c.6 0 1 .4 1 1 0 1.3.2 2.5.6 3.6.1.3 0 .7-.2 1z"/></svg>
      <span>555-014-2270</span>
    </div>
    <div class="contact-email">
      <svg width="18" height="12" viewBox="0 0 18 12"><rect width="18" height="12" fill="var(--ink)"/><path d="M0 0l9 7 9-7" stroke="var(--yellow)" stroke-width="1.4" fill="none"/></svg>
      <span>marla@trelvanesummitconsulting.com</span>
    </div>
  </footer>
</main>
</body>
</html>
```